Supplement Company needs final product mockups and label design

We're a Supplement company launching 4 Hydration Supplement flavours. We need someone to re create the EXACT design with what ChatGPT has already generated and tweak the design slightly so that spelling is correct and callout icons are designed. We then also need someone to do the back of label design that includes space for the barcode, nutrition table, blurb etc. Bonus if you have experience with PLDWX compliance regulations and designing supplement labels.

We want the other 3 flavours (Lime, Mango & Watermelon) to match the design of the strawberry flavour including details like all the callout icons on the left side of the front, the word "electrolytes" in the dark coloured box, the words "hydration powder" just above the callout icons. Please re - design the callout icons to better suit the callout.

I've also attached an image of what the nutrition label should look like.

Please include the Following on the back of the label:
"Directions: Mix 1 Scoop with 400-500ml of water & Mix well before drinking. Do not exceed 2 servings per day.

Why live when you can QORVEL?
Your body wasn’t made to run on sugar, chemicals, and artificial junk — and your hydration shouldn’t either. At QORVEL Nutrition, we’ve created a clean, mineral-rich formula with Brannock Shore Salt and essential electrolytes to fuel you the right way. No toxins, no fillers — just real ingredients that work with your body, not against it.
Hydrate the way nature intended. Live clean. QORVEL.

AUSTRALIAN OWNED AND MADE

Store in a cool, dry place below 30°C. Reseal after use"

Product Formula & Ingredients:

* Sodium (Sea Salt, Brannock Shore Salt®, Himalayan Pink Salt): 1000 mg
* Potassium (from Potassium Chloride): 200 mg
* Magnesium (from Magnesium Glycinate): 60 mg
* Total Carbohydrates: 0 g
* Sugars: 0 g
* Calories: 1 kcal

Ingredients:
Sea Salt, Citric Acid, Brannock Shore Salt®, Himalayan Pink Salt, Potassium Chloride, Magnesium Glycinate, Natural Flavour (e.g. Mango), Stevia Leaf Extract.
Updates

I would like to give designers more time to closely replicate what I have included in the brief and make sure they can create something very beautifully

Industry/Entity Type

Supplements

Font styles to use
Other font styles liked:
• Montserrat

Requirements
Must have
• Back of label design aswell and Australian Nutrition table
Nice to have
• Design as close to the Provided images as possible
Should not have
• Should not be too different to the attached images

```html
<!DOCTYPE html>
<html lang="en">
<head>
<meta charset="utf-8">
<title>QORVEL Nutrition – Electrolytes Labels</title>
<link href="https://fonts.googleapis.com/css2?family=Anton&family=Montserrat:wght@300;500;700;800&family=Roboto+Condensed:wght@400;700&family=Arimo:wght@400;700&display=swap" rel="stylesheet">
<style>
  :root{
    --strawberry:#e3131c; --strawberry-dark:#6e0a0b;
    --watermelon:#e0258d; --watermelon-dark:#86104c;
    --lime:#2fae3b; --lime-dark:#0b5e25;
    --mango:#f2a516; --mango-dark:#b25a06;
    --ink:#111111; --paper:#ffffff;
  }
  *{box-sizing:border-box;margin:0;padding:0}
  html,body{width:703px;height:1200px;overflow:hidden;background:var(--paper)}
  body{position:relative;font-family:"Arimo",Arial,sans-serif;color:var(--paper)}

  .label{position:absolute;width:624px;height:200px;overflow:hidden;
    background:linear-gradient(105deg,var(--dark) 0%,var(--main) 24%,var(--main) 68%,var(--dark) 100%);}
  .label::before{content:"";position:absolute;inset:0;
    background:linear-gradient(160deg,rgba(255,255,255,.10) 0%,rgba(255,255,255,0) 40%,rgba(0,0,0,.12) 100%);}
  .label--strawberry{--main:var(--strawberry);--dark:var(--strawberry-dark);left:35px;top:127px}
  .label--watermelon{--main:var(--watermelon);--dark:var(--watermelon-dark);left:35px;top:387px}
  .label--lime{--main:var(--lime);--dark:var(--lime-dark);left:30px;top:641px}
  .label--mango{--main:var(--mango);--dark:var(--mango-dark);left:32px;top:897px}
  .label--mango .facts,.label--mango .flavour,.label--mango .marketed,.label--mango .other-ingredients{color:var(--ink)}
  .label--mango .facts{border-color:rgba(0,0,0,.35)}
  .label--mango .facts .rule{background:rgba(0,0,0,.6)}
  .label--mango .usage{color:#2a1700}
  .label--mango .usage .note{border-color:#2a1700}

  /* left column */
  .usage{position:absolute;left:32px;top:18px;width:123px;font-size:5.1px;line-height:7.3px;text-align:justify}
  .usage p{margin-bottom:3.4px}
  .usage b{font-weight:700}
  .usage .note{border:.6px solid currentColor;border-radius:2px;padding:1px 1px;margin-bottom:3.6px;text-align:left}
  .usage .footer-note{margin-top:14px;text-align:center;font-size:4.4px;line-height:5.8px}

  /* centre */
  .brand{position:absolute;left:206px;width:200px;top:18px;text-align:center;font-family:"Montserrat",sans-serif;font-weight:800;font-size:22px;letter-spacing:.5px;line-height:24px}
  .brand-sub{position:absolute;left:206px;width:200px;top:44px;text-align:center;font-family:"Montserrat",sans-serif;font-weight:300;font-size:8.6px;letter-spacing:2.6px}
  .flavour{position:absolute;left:156px;width:300px;top:54px;text-align:center;font-family:"Anton",sans-serif;font-size:31px;line-height:42px;letter-spacing:1px}
  .electrolytes{position:absolute;left:231px;top:90px;width:153px;height:21px;border-radius:6px;background:var(--ink);
    font-family:"Montserrat",sans-serif;font-weight:700;font-size:12.6px;letter-spacing:1.9px;line-height:21px;text-align:center}
  .powder{position:absolute;left:205px;top:114px;font-family:"Montserrat",sans-serif;font-weight:700;font-size:7.4px;line-height:10px}
  .callouts{position:absolute;left:205px;top:136px;list-style:none;font-family:"Montserrat",sans-serif;font-weight:700;font-size:7px}
  .callouts li{display:flex;align-items:center;height:14px;gap:5px}
  .callouts svg{width:10px;height:10px}
  .fruit{position:absolute;left:298px;top:112px;width:68px;height:68px;border-radius:50%}
  .net{position:absolute;left:281px;top:181px;font-family:"Montserrat",sans-serif;font-weight:700;font-size:7.4px;letter-spacing:.4px}

  /* right column */
  .facts{position:absolute;left:472px;top:20px;width:121px;height:114px;border:.7px solid rgba(255,255,255,.8);padding:3px 6px;font-family:"Roboto Condensed",sans-serif}
  .facts h2{font-weight:700;font-size:10.6px;line-height:12px}
  .facts .serving{font-size:3.4px;line-height:4.2px;font-weight:700}
  .facts .rule{height:1.3px;background:rgba(255,255,255,.9);margin:1px 0}
  .facts .row{display:grid;grid-template-columns:1fr 14px 18px;font-size:3.4px;line-height:5.6px;border-bottom:.4px solid rgba(255,255,255,.55)}
  .facts .row span:nth-child(2),.facts .row span:nth-child(3){text-align:right}
  .facts .row.head{font-size:2.6px;line-height:4px}
  .facts .row.cal{font-size:6px;line-height:7px;font-weight:700}
  .facts .row.bold span:first-child{font-weight:700}
  .facts .row.sub span:first-child{padding-left:3px}
  .facts .foot{font-size:3px;line-height:6px;font-weight:700}

  .other-ingredients{position:absolute;left:476px;top:137px;width:118px;font-size:3.4px;line-height:4.3px}
  .other-ingredients b{font-weight:700}
  .marketed{position:absolute;left:476px;top:157px;font-size:4.8px;line-height:5.5px}
  .marketed b{font-weight:700}
  .pack-icons{position:absolute;left:563px;top:157px;display:flex;gap:4px}
  .pack-icons svg{width:8px;height:8px}
</style>
</head>
<body>

<!-- Strawberry -->
<section class="label label--strawberry">
  <div class="usage">
    <p><b>DIRECTIONS:</b> As a convenient source of Omega-3 Fatty Acids (EPA and DHA), take 1 softgel three times a day.</p>
    <p><b>WARNING:</b> Do no take this product if you have or have had a recent surgery or bleeding disorder, are pregnant or lactating, or are taking blood thinning drugs.</p>
    <p class="note">Lorem ipsum dolor sit amet, consectetuer adipiscing elit, sed diam nonummy nibh euismod tincidunt ut laoreet dolore magna aliquam erat volutpat.</p>
    <p><b>Lorem ipsum dolor sit amet, consectetuer adipiscing elit, sed diam nonummy nibh euismod tincidunt.</b></p>
    <p><b>STORAGE:</b> Keep out of reach of children. Do not use if safety seal is damaged or missing. Stored in a cool, dry place.</p>
    <p class="footer-note">Lorem ipsum dolor sit amet, consectetuer adipiscing elit, sed diam nonummy nibh euismod.</p>
  </div>
  <div class="brand">QORVEL</div>
  <div class="brand-sub">NUTRITION</div>
  <div class="flavour">STRAWBERRY</div>
  <div class="electrolytes">ELECTROLYTES</div>
  <div class="powder">HYDRATION<br>POWDER</div>
  <ul class="callouts">
    <li><svg viewBox="0 0 10 10"><circle cx="5" cy="5" r="5" fill="#111"/><path d="M3 7l4-4M3.5 3.5h3v3" stroke="#fff" stroke-width=".8" fill="none"/></svg>KETO FREE</li>
    <li><svg viewBox="0 0 10 10"><circle cx="5" cy="5" r="5" fill="#111"/><path d="M5 2.2v5.6M3.6 3.6l1.4 1M6.4 3.6L5 4.6M3.6 5.4l1.4 1M6.4 5.4L5 6.4M2.5 7.5l5-5" stroke="#fff" stroke-width=".7" fill="none"/></svg>GLUTEN FREE</li>
    <li><svg viewBox="0 0 10 10"><circle cx="5" cy="5" r="5" fill="#111"/><rect x="3" y="3.2" width="4" height="3.6" fill="none" stroke="#fff" stroke-width=".7"/><path d="M2.4 7.6l5.2-5.2" stroke="#fff" stroke-width=".7"/></svg>SUGAR FREE</li>
    <li><svg viewBox="0 0 10 10"><circle cx="5" cy="5" r="5" fill="#111"/><ellipse cx="5" cy="5" rx="2.6" ry="2" fill="none" stroke="#fff" stroke-width=".7"/><path d="M3.6 5.6l2.8-1.2" stroke="#fff" stroke-width=".7"/></svg>PALED FREE</li>
  </ul>
  <div class="fruit" role="img" aria-label="Photo of a ripe strawberry" style="background:radial-gradient(circle at 45% 45%,#ff4a3a,#b80d10 70%,rgba(184,13,16,0) 72%)"></div>
  <div class="net">NET WT.180G</div>
  <div class="facts">
    <h2>Supplement Facts</h2>
    <div class="serving">Serving Size: 1 Capsule<br>Servings Per Container 60</div>
    <div class="rule"></div>
    <div class="row head"><span>Amount Per Serving</span><span></span><span>% Daily Value</span></div>
    <div class="row cal"><span>Calories</span><span></span><span>245</span></div>
    <div class="row bold"><span>Total Fat</span><span></span><span>0%</span></div>
    <div class="row sub"><span>Saturated Fat</span><span>0g</span><span>0%</span></div>
    <div class="row sub"><span>Trans Fat</span><span>0g</span><span></span></div>
    <div class="row bold"><span>Cholesterol</span><span>0mg</span><span>0%</span></div>
    <div class="row bold"><span>Sodium</span><span>0mg</span><span>0%</span></div>
    <div class="row bold"><span>Total Carbohydrate</span><span></span><span>0%</span></div>
    <div class="row sub"><span>Dietary Fiber</span><span>0g</span><span></span></div>
    <div class="row sub"><span>Sugars</span><span>0g</span><span></span></div>
    <div class="row bold"><span>Protein</span><span>0g</span><span></span></div>
    <div class="foot">*Persent Daily Values are based on a 2,400 calories diet</div>
  </div>
  <p class="other-ingredients"><b>OTHER INGREDIENTS:</b> Lorem ipsum dolor sit amet, consectetuer adipiscing elit, sed diam nonummy nibh euismod. euismod tincidunt ut laoreet dolore.</p>
  <p class="marketed"><b>Marketed By:</b><br>Your Company name<br>Your Area Address, Your City<br>Lic No. 17840825785</p>
  <div class="pack-icons"><svg viewBox="0 0 8 8"><circle cx="4" cy="4" r="3" fill="none" stroke="currentColor" stroke-width=".9"/></svg><svg viewBox="0 0 8 8"><path d="M1.5 2h5M3 2V1h2v1M2.2 2.5l.5 5h2.6l.5-5" fill="none" stroke="currentColor" stroke-width=".7"/></svg></div>
</section>

<!-- Watermelon -->
<section class="label label--watermelon">
  <div class="usage">
    <p><b>DIRECTIONS:</b> As a convenient source of Omega-3 Fatty Acids (EPA and DHA), take 1 softgel three times a day.</p>
    <p><b>WARNING:</b> Do no take this product if you have or have had a recent surgery or bleeding disorder, are pregnant or lactating, or are taking blood thinning drugs.</p>
    <p class="note">Lorem ipsum dolor sit amet, consectetuer adipiscing elit, sed diam nonummy nibh euismod tincidunt ut laoreet dolore magna aliquam erat volutpat.</p>
    <p><b>Lorem ipsum dolor sit amet, consectetuer adipiscing elit, sed diam nonummy nibh euismod tincidunt.</b></p>
    <p><b>STORAGE:</b> Keep out of reach of children. Do not use if safety seal is damaged or missing. Stored in a cool, dry place.</p>
    <p class="footer-note">Lorem ipsum dolor sit amet, consectetuer adipiscing elit, sed diam nonummy nibh euismod.</p>
  </div>
  <div class="brand">QORVEL</div>
  <div class="brand-sub">NUTRITION</div>
  <div class="flavour">WATERMELON</div>
  <div class="electrolytes">ELECTROLYTES</div>
  <div class="powder">HYDRATION<br>POWDER</div>
  <ul class="callouts">
    <li><svg viewBox="0 0 10 10"><circle cx="5" cy="5" r="5" fill="#111"/><path d="M3 7l4-4M3.5 3.5h3v3" stroke="#fff" stroke-width=".8" fill="none"/></svg>KETO FREE</li>
    <li><svg viewBox="0 0 10 10"><circle cx="5" cy="5" r="5" fill="#111"/><path d="M5 2.2v5.6M3.6 3.6l1.4 1M6.4 3.6L5 4.6M3.6 5.4l1.4 1M6.4 5.4L5 6.4M2.5 7.5l5-5" stroke="#fff" stroke-width=".7" fill="none"/></svg>GLUTEN FREE</li>
    <li><svg viewBox="0 0 10 10"><circle cx="5" cy="5" r="5" fill="#111"/><rect x="3" y="3.2" width="4" height="3.6" fill="none" stroke="#fff" stroke-width=".7"/><path d="M2.4 7.6l5.2-5.2" stroke="#fff" stroke-width=".7"/></svg>SUGAR FREE</li>
    <li><svg viewBox="0 0 10 10"><circle cx="5" cy="5" r="5" fill="#111"/><ellipse cx="5" cy="5" rx="2.6" ry="2" fill="none" stroke="#fff" stroke-width=".7"/><path d="M3.6 5.6l2.8-1.2" stroke="#fff" stroke-width=".7"/></svg>PALED FREE</li>
  </ul>
  <div class="fruit" role="img" aria-label="Photo of a whole watermelon and a red slice" style="background:radial-gradient(circle at 40% 45%,#3c8a3a,#123f1c 60%,rgba(18,63,28,0) 72%),radial-gradient(circle at 75% 65%,#e8323a 0,#e8323a 20%,rgba(232,50,58,0) 30%)"></div>
  <div class="net">NET WT.180G</div>
  <div class="facts">
    <h2>Supplement Facts</h2>
    <div class="serving">Serving Size: 1 Capsule<br>Servings Per Container 60</div>
    <div class="rule"></div>
    <div class="row head"><span>Amount Per Serving</span><span></span><span>% Daily Value</span></div>
    <div class="row cal"><span>Calories</span><span></span><span>245</span></div>
    <div class="row bold"><span>Total Fat</span><span></span><span>0%</span></div>
    <div class="row sub"><span>Saturated Fat</span><span>0g</span><span>0%</span></div>
    <div class="row sub"><span>Trans Fat</span><span>0g</span><span></span></div>
    <div class="row bold"><span>Cholesterol</span><span>0mg</span><span>0%</span></div>
    <div class="row bold"><span>Sodium</span><span>0mg</span><span>0%</span></div>
    <div class="row bold"><span>Total Carbohydrate</span><span></span><span>0%</span></div>
    <div class="row sub"><span>Dietary Fiber</span><span>0g</span><span></span></div>
    <div class="row sub"><span>Sugars</span><span>0g</span><span></span></div>
    <div class="row bold"><span>Protein</span><span>0g</span><span></span></div>
    <div class="foot">*Persent Daily Values are based on a 2,400 calories diet</div>
  </div>
  <p class="other-ingredients"><b>OTHER INGREDIENTS:</b> Lorem ipsum dolor sit amet, consectetuer adipiscing elit, sed diam nonummy nibh euismod. euismod tincidunt ut laoreet dolore.</p>
  <p class="marketed"><b>Marketed By:</b><br>Your Company name<br>Your Area Address, Your City<br>Lic No. 17840825785</p>
  <div class="pack-icons"><svg viewBox="0 0 8 8"><circle cx="4" cy="4" r="3" fill="none" stroke="currentColor" stroke-width=".9"/></svg><svg viewBox="0 0 8 8"><path d="M1.5 2h5M3 2V1h2v1M2.2 2.5l.5 5h2.6l.5-5" fill="none" stroke="currentColor" stroke-width=".7"/></svg></div>
</section>

<!-- Lime -->
<section class="label label--lime">
  <div class="usage">
    <p><b>DIRECTIONS:</b> As a convenient source of Omega-3 Fatty Acids (EPA and DHA), take 1 softgel three times a day.</p>
    <p><b>WARNING:</b> Do no take this product if you have or have had a recent surgery or bleeding disorder, are pregnant or lactating, or are taking blood thinning drugs.</p>
    <p class="note">Lorem ipsum dolor sit amet, consectetuer adipiscing elit, sed diam nonummy nibh euismod tincidunt ut laoreet dolore magna aliquam erat volutpat.</p>
    <p><b>Lorem ipsum dolor sit amet, consectetuer adipiscing elit, sed diam nonummy nibh euismod tincidunt.</b></p>
    <p><b>STORAGE:</b> Keep out of reach of children. Do not use if safety seal is damaged or missing. Stored in a cool, dry place.</p>
    <p class="footer-note">Lorem ipsum dolor sit amet, consectetuer adipiscing elit, sed diam nonummy nibh euismod.</p>
  </div>
  <div class="brand">QORVEL</div>
  <div class="brand-sub">NUTRITION</div>
  <div class="flavour">LIME</div>
  <div class="electrolytes">ELECTROLYTES</div>
  <div class="powder">HYDRATION<br>POWDER</div>
  <ul class="callouts">
    <li><svg viewBox="0 0 10 10"><circle cx="5" cy="5" r="5" fill="#111"/><path d="M3 7l4-4M3.5 3.5h3v3" stroke="#fff" stroke-width=".8" fill="none"/></svg>KETO FREE</li>
    <li><svg viewBox="0 0 10 10"><circle cx="5" cy="5" r="5" fill="#111"/><path d="M5 2.2v5.6M3.6 3.6l1.4 1M6.4 3.6L5 4.6M3.6 5.4l1.4 1M6.4 5.4L5 6.4M2.5 7.5l5-5" stroke="#fff" stroke-width=".7" fill="none"/></svg>GLUTEN FREE</li>
    <li><svg viewBox="0 0 10 10"><circle cx="5" cy="5" r="5" fill="#111"/><rect x="3" y="3.2" width="4" height="3.6" fill="none" stroke="#fff" stroke-width=".7"/><path d="M2.4 7.6l5.2-5.2" stroke="#fff" stroke-width=".7"/></svg>SUGAR FREE</li>
    <li><svg viewBox="0 0 10 10"><circle cx="5" cy="5" r="5" fill="#111"/><ellipse cx="5" cy="5" rx="2.6" ry="2" fill="none" stroke="#fff" stroke-width=".7"/><path d="M3.6 5.6l2.8-1.2" stroke="#fff" stroke-width=".7"/></svg>PALED FREE</li>
  </ul>
  <div class="fruit" role="img" aria-label="Photo of whole and halved limes with leaves" style="background:radial-gradient(circle at 45% 55%,#d8f07a,#7cc23a 45%,#2f7a22 65%,rgba(47,122,34,0) 72%)"></div>
  <div class="net">NET WT.180G</div>
  <div class="facts">
    <h2>Supplement Facts</h2>
    <div class="serving">Serving Size: 1 Capsule<br>Servings Per Container 60</div>
    <div class="rule"></div>
    <div class="row head"><span>Amount Per Serving</span><span></span><span>% Daily Value</span></div>
    <div class="row cal"><span>Calories</span><span></span><span>245</span></div>
    <div class="row bold"><span>Total Fat</span><span></span><span>0%</span></div>
    <div class="row sub"><span>Saturated Fat</span><span>0g</span><span>0%</span></div>
    <div class="row sub"><span>Trans Fat</span><span>0g</span><span></span></div>
    <div class="row bold"><span>Cholesterol</span><span>0mg</span><span>0%</span></div>
    <div class="row bold"><span>Sodium</span><span>0mg</span><span>0%</span></div>
    <div class="row bold"><span>Total Carbohydrate</span><span></span><span>0%</span></div>
    <div class="row sub"><span>Dietary Fiber</span><span>0g</span><span></span></div>
    <div class="row sub"><span>Sugars</span><span>0g</span><span></span></div>
    <div class="row bold"><span>Protein</span><span>0g</span><span></span></div>
    <div class="foot">*Persent Daily Values are based on a 2,400 calories diet</div>
  </div>
  <p class="other-ingredients"><b>OTHER INGREDIENTS:</b> Lorem ipsum dolor sit amet, consectetuer adipiscing elit, sed diam nonummy nibh euismod. euismod tincidunt ut laoreet dolore.</p>
  <p class="marketed"><b>Marketed By:</b><br>Your Company name<br>Your Area Address, Your City<br>Lic No. 17840825785</p>
  <div class="pack-icons"><svg viewBox="0 0 8 8"><circle cx="4" cy="4" r="3" fill="none" stroke="currentColor" stroke-width=".9"/></svg><svg viewBox="0 0 8 8"><path d="M1.5 2h5M3 2V1h2v1M2.2 2.5l.5 5h2.6l.5-5" fill="none" stroke="currentColor" stroke-width=".7"/></svg></div>
</section>

<!-- Mango -->
<section class="label label--mango">
  <div class="usage">
    <p><b>DIRECTIONS:</b> As a convenient source of Omega-3 Fatty Acids (EPA and DHA), take 1 softgel three times a day.</p>
    <p><b>WARNING:</b> Do no take this product if you have or have had a recent surgery or bleeding disorder, are pregnant or lactating, or are taking blood thinning drugs.</p>
    <p class="note">Lorem ipsum dolor sit amet, consectetuer adipiscing elit, sed diam nonummy nibh euismod tincidunt ut laoreet dolore magna aliquam erat volutpat.</p>
    <p><b>Lorem ipsum dolor sit amet, consectetuer adipiscing elit, sed diam nonummy nibh euismod tincidunt.</b></p>
    <p><b>STORAGE:</b> Keep out of reach of children. Do not use if safety seal is damaged or missing. Stored in a cool, dry place.</p>
    <p class="footer-note">Lorem ipsum dolor sit amet, consectetuer adipiscing elit, sed diam nonummy nibh euismod.</p>
  </div>
  <div class="brand">QORVEL</div>
  <div class="brand-sub">NUTRITION</div>
  <div class="flavour">MANGO</div>
  <div class="electrolytes">ELECTROLYTES</div>
  <div class="powder">HYDRATION<br>POWDER</div>
  <ul class="callouts">
    <li><svg viewBox="0 0 10 10"><circle cx="5" cy="5" r="5" fill="#111"/><path d="M3 7l4-4M3.5 3.5h3v3" stroke="#fff" stroke-width=".8" fill="none"/></svg>KETO FREE</li>
    <li><svg viewBox="0 0 10 10"><circle cx="5" cy="5" r="5" fill="#111"/><path d="M5 2.2v5.6M3.6 3.6l1.4 1M6.4 3.6L5 4.6M3.6 5.4l1.4 1M6.4 5.4L5 6.4M2.5 7.5l5-5" stroke="#fff" stroke-width=".7" fill="none"/></svg>GLUTEN FREE</li>
    <li><svg viewBox="0 0 10 10"><circle cx="5" cy="5" r="5" fill="#111"/><rect x="3" y="3.2" width="4" height="3.6" fill="none" stroke="#fff" stroke-width=".7"/><path d="M2.4 7.6l5.2-5.2" stroke="#fff" stroke-width=".7"/></svg>SUGAR FREE</li>
    <li><svg viewBox="0 0 10 10"><circle cx="5" cy="5" r="5" fill="#111"/><ellipse cx="5" cy="5" rx="2.6" ry="2" fill="none" stroke="#fff" stroke-width=".7"/><path d="M3.6 5.6l2.8-1.2" stroke="#fff" stroke-width=".7"/></svg>PALED FREE</li>
  </ul>
  <div class="fruit" role="img" aria-label="Photo of a ripe mango with a leaf" style="background:radial-gradient(ellipse at 55% 55%,#ffc23a,#e07d12 55%,rgba(224,125,18,0) 70%)"></div>
  <div class="net">NET WT.180G</div>
  <div class="facts">
    <h2>Supplement Facts</h2>
    <div class="serving">Serving Size: 1 Capsule<br>Servings Per Container 60</div>
    <div class="rule"></div>
    <div class="row head"><span>Amount Per Serving</span><span></span><span>% Daily Value</span></div>
    <div class="row cal"><span>Calories</span><span></span><span>245</span></div>
    <div class="row bold"><span>Total Fat</span><span></span><span>0%</span></div>
    <div class="row sub"><span>Saturated Fat</span><span>0g</span><span>0%</span></div>
    <div class="row sub"><span>Trans Fat</span><span>0g</span><span></span></div>
    <div class="row bold"><span>Cholesterol</span><span>0mg</span><span>0%</span></div>
    <div class="row bold"><span>Sodium</span><span>0mg</span><span>0%</span></div>
    <div class="row bold"><span>Total Carbohydrate</span><span></span><span>0%</span></div>
    <div class="row sub"><span>Dietary Fiber</span><span>0g</span><span></span></div>
    <div class="row sub"><span>Sugars</span><span>0g</span><span></span></div>
    <div class="row bold"><span>Protein</span><span>0g</span><span></span></div>
    <div class="foot">*Persent Daily Values are based on a 2,400 calories diet</div>
  </div>
  <p class="other-ingredients"><b>OTHER INGREDIENTS:</b> Lorem ipsum dolor sit amet, consectetuer adipiscing elit, sed diam nonummy nibh euismod. euismod tincidunt ut laoreet dolore.</p>
  <p class="marketed"><b>Marketed By:</b><br>Your Company name<br>Your Area Address, Your City<br>Lic No. 17840825785</p>
  <div class="pack-icons" style="color:#111"><svg viewBox="0 0 8 8"><circle cx="4" cy="4" r="3" fill="none" stroke="currentColor" stroke-width=".9"/></svg><svg viewBox="0 0 8 8"><path d="M1.5 2h5M3 2V1h2v1M2.2 2.5l.5 5h2.6l.5-5" fill="none" stroke="currentColor" stroke-width=".7"/></svg></div>
</section>

</body>
</html>
```